Namecard Designs+Logo for a High End Automobile Company

We need a new business card for our company called Velta Motorhof.

www.veltamotorhof.example.sg
Our new website will be up in 2.5 months time.

We sell used and brand new continental cars like Korvane, QTL, Dravell, Solbrini and etc. Currently we are operating from 2 offices in Singapore and United Kingdom.

We want a design which is serious. We are open to colours but try to keep it at a maximum of 3 colours.

We prefer something simple and minimal. We are open to 2 sides printing or even 2 sided namecards. Both UK and Singapore company offices address must be in; either side by side, front and back, or even 2 sided cards.

The logo can be a text logo, emblem, abstract, pictorial or combination.

We are printing with Pribo.com so please kindly follow the printing guideline.

http://uk.pribo.example/help/faq/templates-and-guidelines.html

Rich and Car Enthusiasts

Printing

Must have
• Our 2 offices; UK and Singapore.

Our slogan which is " The Automobile Specialist"
Should not have
• Not more than 3 colours

```html
<!DOCTYPE html>
<html lang="en">
<head>
<meta charset="utf-8">
<title>Velta Motorhof – Business Card</title>
<link href="https://fonts.googleapis.com/css2?family=Arimo:wght@400;700&family=Courier+Prime&display=swap" rel="stylesheet">
<style>
  :root {
    --page: #ffffff;
    --card-dark: #6f6f6f;
    --card-mid: #8e8e8e;
    --card-light: #a9a9a9;
    --band: rgba(225, 225, 225, 0.72);
    --ink-light: #ffffff;
    --ink-soft: #d9d9d9;
    --ink-dark: #3a3a3a;
    --label: #111111;
  }
  * { margin: 0; padding: 0; box-sizing: border-box; }
  html, body {
    width: 1200px; height: 624px; overflow: hidden;
    background: var(--page);
  }
  .canvas { position: relative; width: 1200px; height: 624px; }

  .card {
    position: absolute; top: 123px;
    width: 540px; height: 352px; overflow: hidden;
  }
  .card--front { left: 61px; }
  .card--back { left: 618px; }

  .card__surface {
    position: absolute; inset: 0;
    background: linear-gradient(160deg, var(--card-mid) 0%, var(--card-light) 45%, var(--card-dark) 100%);
  }

  .brand {
    position: absolute; display: flex; align-items: center;
    font-family: "Arimo", Arial, sans-serif; font-weight: 700;
    color: var(--ink-light); white-space: nowrap;
  }
  .brand__disc {
    border-radius: 50%; background: var(--ink-light); flex: none;
  }
  .brand--front { left: 46px; top: 111px; gap: 10px; font-size: 36px; letter-spacing: -0.5px; }
  .brand--front .brand__disc { width: 114px; height: 114px; }
  .brand--back { left: 346px; top: 31px; gap: 5px; font-size: 16px; }
  .brand--back .brand__disc { width: 48px; height: 48px; }

  .front-url {
    position: absolute; left: 0; right: 0; top: 318px; text-align: center;
    font-family: "Arimo", Arial, sans-serif; font-weight: 700;
    font-size: 15px; letter-spacing: 2.4px; color: var(--ink-soft);
  }

  .back-ring {
    position: absolute; left: -40px; top: -41px; width: 240px; height: 240px;
    border-radius: 50%; border: 11px solid rgba(255,255,255,0.22);
    background: rgba(255,255,255,0.12);
  }

  .contact-band {
    position: absolute; left: 0; right: 0; top: 207px; height: 106px;
    background: var(--band);
  }
  .contact {
    position: absolute; top: 222px;
    font-family: "Courier Prime", "Courier New", monospace;
    font-size: 10.5px; line-height: 14px; color: var(--ink-dark);
    list-style: none; white-space: nowrap;
  }
  .contact--uk { left: 11px; }
  .contact--sg { right: 6px; top: 224px; text-align: right; }

  .side-label {
    position: absolute; top: 497px; width: 200px; text-align: center;
    font-family: "Arimo", Arial, sans-serif; font-size: 22px; color: var(--label);
  }
  .side-label--front { left: 231px; }
  .side-label--back { left: 792px; }
</style>
</head>
<body>
<main class="canvas">
  <section class="card card--front" aria-label="Card front">
    <div class="card__surface"></div>
    <div class="brand brand--front">
      <span class="brand__disc"></span>
      <span class="brand__name">Velta Motorhof.</span>
    </div>
    <p class="front-url">http://www.veltamotorhof.example.sg</p>
  </section>

  <section class="card card--back" aria-label="Card back">
    <div class="card__surface"></div>
    <div class="back-ring"></div>
    <div class="brand brand--back">
      <span class="brand__disc"></span>
      <span class="brand__name">Velta Motorhof.</span>
    </div>
    <div class="contact-band"></div>
    <ul class="contact contact--uk">
      <li>Ph: (02) 4100 2391</li>
      <li>Fax: (02) 4100 2392</li>
      <li>Email: mail@veltamotorhof.example.sg</li>
      <li>Website:www.veltamotorhof.example.sg</li>
      <li>Address: sample 318, UK</li>
      <li>Postal Address: PO BOX 2184, UK</li>
    </ul>
    <ul class="contact contact--sg">
      <li>Ph: (02) 3100 7415</li>
      <li>Fax: (02) 3100 7416</li>
      <li>Email: office@veltamotorhof.example.sg</li>
      <li>Website:www.veltamotorhof.example.sg</li>
      <li>Address: sample 318, Singapore</li>
      <li>Postal Address: PO BOX 4470, Singapore</li>
    </ul>
  </section>

  <p class="side-label side-label--front">front</p>
  <p class="side-label side-label--back">back</p>
</main>
</body>
</html>
```